Website design

Hi I'm looking for someone to create a website for me using wordpress that is similar tothis site but not exactly the same. The reason I want it done in wordpress is so I can edit it if need be. Cheers

http://freequote.bramblewoodlop.com.au/?gclid=XqTRbN7LpW2mZkVc8HdJ4sFyGtQe9UoA3iBxC5nMzKa1rPlYfDw6vEgHtJ0bNsWuCyRoQd_KxZ

My current website is www.kestrelgroveprune.com.au

Target Market(s)

tree care industry

Number of Pages Required

1 page

```html
<!DOCTYPE html>
<html lang="en">
<head>
<meta charset="utf-8">
<title>Kestrel Grove Tree Surgeons</title>
<link href="https://fonts.googleapis.com/css2?family=Roboto:wght@400;500;700;900&family=Open+Sans:wght@400;600;700&display=swap" rel="stylesheet">
<style>
:root{
  --green:#1fa54a;
  --green-dark:#16883b;
  --red:#e3312a;
  --ink:#222222;
  --text:#555555;
  --muted:#8a8a8a;
  --grey:#efefef;
  --grey-2:#f5f5f5;
  --white:#ffffff;
  --blue:#2a5ea8;
}
*{box-sizing:border-box;margin:0;padding:0}
html,body{width:1200px;height:4358px;overflow:hidden}
body{font-family:"Open Sans",sans-serif;color:var(--text);background:var(--white);position:relative}
h1,h2,h3,h4,.btn,.nav a{font-family:"Roboto",sans-serif}
section,header,footer{position:relative;width:1200px;overflow:hidden}
.abs{position:absolute}
.btn{position:absolute;display:flex;align-items:center;justify-content:center;background:var(--red);color:var(--white);font-weight:500;font-size:14px;border-radius:3px;text-transform:uppercase;letter-spacing:.3px}
.photo{position:absolute}

/* header */
.site-header{height:118px;background:var(--white);z-index:3;overflow:visible}
.brand{position:absolute;left:70px;top:-40px;width:220px;height:220px;border-radius:50%;background:var(--white);display:flex;align-items:center;justify-content:center;gap:8px;padding-top:40px}
.brand-mark{width:18px;height:18px;border-radius:50%;background:var(--green)}
.brand-name{font-family:"Roboto",sans-serif;font-weight:700;font-size:18px;line-height:1.15;color:var(--blue);width:130px}
.topline{position:absolute;left:688px;top:28px;display:flex;align-items:center;gap:12px;font-size:16px;color:var(--ink)}
.nav{position:absolute;right:100px;top:80px;display:flex;gap:28px}
.nav a{font-size:15px;font-weight:700;color:var(--ink);text-decoration:none;text-transform:uppercase}

/* hero */
.hero{height:577px;margin-top:-2px}
.hero .photo{inset:0;background:linear-gradient(100deg,#3b3a2c 0%,#5a5a3e 35%,#3d4a2e 60%,#263021 100%)}
.hero h1{position:absolute;left:100px;top:224px;color:var(--white);font-size:42px;font-weight:900;line-height:46px;text-transform:uppercase}
.dots{position:absolute;left:100px;top:402px;display:flex;gap:8px}
.dots span{width:13px;height:13px;border-radius:50%;border:2px solid var(--white)}
.dots span:first-child{background:var(--white)}
.quote-form{position:absolute;left:773px;top:44px;width:325px;height:485px;background:rgba(20,25,30,.85);border:2px solid rgba(255,255,255,.25);padding:24px 22px}
.quote-form h3{color:var(--white);font-size:23px;font-weight:500;line-height:28px}
.quote-form .sub{color:var(--white);font-family:"Roboto",sans-serif;font-weight:700;font-size:17px;margin-bottom:18px}
.field label{display:block;color:var(--white);font-size:13px;margin-bottom:5px}
.field div{height:38px;background:var(--white);margin-bottom:22px}
.quote-form .submit{position:static;height:40px;width:100%}

/* features */
.features{height:124px;background:var(--green);color:var(--white)}
.feature{position:absolute;top:38px;display:flex;align-items:center;gap:14px;font-size:14px;font-weight:600;line-height:18px}

/* intro */
.intro{height:512px}
.intro .photo{left:100px;top:88px;width:455px;height:308px;background:linear-gradient(160deg,#9ab0c8 0%,#c9d2d8 45%,#7d8a7a 70%,#5a6a55 100%)}
.play{position:absolute;left:310px;top:225px}
.intro .copy{position:absolute;left:598px;top:92px;width:500px;font-size:15px;line-height:27px}
.intro .copy p{margin-bottom:18px}

/* services */
.services{height:694px;background:var(--grey)}
.services .photo{right:0;top:0;width:500px;height:694px;background:linear-gradient(90deg,rgba(239,239,239,1) 0%,rgba(200,205,190,.6) 60%,rgba(180,190,170,.5) 100%)}
.section-title{position:absolute;left:0;width:1200px;text-align:center;color:var(--ink);font-size:33px;font-weight:500;text-transform:uppercase}
.rule{position:absolute;left:565px;width:70px;height:2px;background:var(--ink)}
.service{position:absolute;width:330px}
.service .icon{width:84px;height:84px;border-radius:50%;background:var(--green);display:flex;align-items:center;justify-content:center}
.service h4{position:absolute;left:103px;top:22px;color:var(--ink);font-size:19px;font-weight:500;line-height:24px;text-transform:uppercase}
.service p{font-size:13px;line-height:22px;margin-top:16px}

/* banner */
.banner{height:404px}
.banner .photo{inset:0;background:linear-gradient(180deg,#2c2a24 0%,#3a3a2c 50%,#22241e 100%)}
.banner h2{position:absolute;left:0;top:92px;width:1200px;text-align:center;color:var(--white);font-size:38px;font-weight:700}
.banner p{position:absolute;left:230px;top:150px;width:740px;text-align:center;color:var(--white);font-size:16px;line-height:30px}

/* guarantee */
.guarantee{height:487px}
.guarantee .panel{position:absolute;left:601px;top:0;width:599px;height:487px;background:var(--grey-2)}
.badge{position:absolute;left:100px;top:90px;width:90px;height:90px;border-radius:50%;background:var(--ink)}
.guarantee h3{position:absolute;color:var(--ink);font-size:21px;font-weight:700;line-height:32px;text-transform:uppercase}
.guarantee .body{position:absolute;left:100px;top:215px;width:490px;font-size:14px;line-height:25px}
.guarantee .body p{margin-bottom:14px}
.ebook{left:640px;top:90px;width:180px;height:349px;background:linear-gradient(135deg,#d7e4c6 0%,#b9cfa1 55%,#92ad7a 100%)}

/* testimonials */
.testimonials{height:453px;background:var(--grey)}
.avatar{left:203px;top:178px;width:170px;height:170px;border-radius:50%;border:5px solid var(--white);background:linear-gradient(160deg,#c9d6e4,#5b7290);box-shadow:0 0 0 2px #1f5c9a}
.testimonial-text{position:absolute;left:459px;top:186px;width:560px;font-size:14.5px;line-height:27px;font-style:italic;color:#777}
.testimonial-name{position:absolute;left:459px;top:320px;font-size:16px;color:var(--ink)}
.qmark{position:absolute;font-family:"Roboto",sans-serif;font-size:110px;color:#d6d6d6;line-height:1}
.arrow{position:absolute;top:228px}

/* blog */
.blog{height:542px}
.blog .photo{left:100px;top:155px;width:437px;height:293px;background:linear-gradient(180deg,#5e88b8 0%,#9db9d6 40%,#4f6a3a 75%,#3b4a2d 100%)}
.blog h3{position:absolute;left:575px;top:162px;width:520px;color:var(--ink);font-size:29px;font-weight:700;line-height:34px;text-transform:uppercase}
.meta{position:absolute;left:575px;top:252px;display:flex;gap:26px;font-size:13px;color:var(--blue);font-style:italic}
.blog .excerpt{position:absolute;left:575px;top:286px;width:525px;font-size:12.5px;line-height:22px;color:#777}
.blog .more{position:absolute;left:575px;top:421px;font-size:12px;color:var(--ink)}

/* call band */
.callband{height:85px;background:var(--green);color:var(--white)}
.callband .label{position:absolute;top:24px;font-size:12px;line-height:16px}
.callband .label b{font-family:"Roboto",sans-serif;font-weight:700;font-size:13px}
.callband .value{position:absolute;top:30px;font-size:18px;font-weight:600}
.or{position:absolute;left:525px;top:24px;width:38px;height:38px;border-radius:50%;background:var(--white);color:var(--green);font-weight:700;font-size:13px;display:flex;align-items:center;justify-content:center}

/* footer */
.site-footer{height:300px;background:var(--white);border-bottom:1px solid #e2e2e2}
.footer-brand{position:absolute;left:100px;top:70px;display:flex;align-items:center;gap:8px}
.site-footer h4{position:absolute;top:62px;color:var(--ink);font-size:19px;font-weight:500;text-transform:uppercase}
.site-footer .small{position:absolute;font-size:13px;color:var(--text)}
.newsletter{position:absolute;left:352px;top:135px;display:flex}
.newsletter .input{width:214px;height:45px;border:1px solid #ddd;display:flex;align-items:center;gap:8px;padding-left:14px;font-size:13px;color:#999}
.newsletter .btn{position:static;width:90px;height:45px;background:var(--green);border-radius:0;font-size:12px;font-weight:700}
.socials{position:absolute;left:352px;top:210px;display:flex;gap:10px}
.socials span{width:36px;height:36px;border-radius:50%;background:var(--blue)}
.links{position:absolute;left:988px;top:103px;list-style:none;font-size:13px;line-height:25px;color:var(--text)}
.links li::before{content:"› ";color:var(--ink)}
.copyright{height:68px;display:flex;align-items:center;justify-content:center;font-size:12px;color:var(--text)}
</style>
</head>
<body>

<header class="site-header">
  <div class="brand"><span class="brand-mark"></span><span class="brand-name">Kestrel Grove Tree Surgeons</span></div>
  <div class="topline">
    <svg width="22" height="22" viewBox="0 0 24 24"><path fill="#e3312a" d="M6.6 10.8a15 15 0 0 0 6.6 6.6l2.2-2.2c.3-.3.7-.4 1-.2 1.1.4 2.300.6 3.6.6.6 0 1 .4 1 1V20c0 .6-.4 1-1 1A17 17 0 0 1 3 4c0-.6.4-1 1-1h3.5c.6 0 1 .4 1 1 0 1.3.2 2.5.6 3.6.1.3 0 .7-.2 1z"/></svg>
    <span>Call Us : 0491 570 156</span>
  </div>
  <a class="btn" style="left:930px;top:23px;width:168px;height:35px;font-size:13px;font-weight:700">Book Online Now</a>
  <nav class="nav">
    <a>Home</a><a>About Us</a><a>Our Services</a><a>Locations</a><a>Blog</a><a>Contact Us</a>
  </nav>
</header>

<section class="hero">
  <div class="photo" role="img" aria-label="Arborist in safety gear preparing ropes beside a tree on a work site"></div>
  <h1>Tree Removal<br>Specialists Kestrel</h1>
  <a class="btn" style="left:100px;top:338px;width:112px;height:38px">Read More</a>
  <div class="dots"><span></span><span></span><span></span></div>
  <form class="quote-form">
    <h3>REQUEST A FREE QUOTE</h3>
    <p class="sub">or Call us 0491 570 156</p>
    <div class="field"><label>First Name *</label><div></div></div>
    <div class="field"><label>Email *</label><div></div></div>
    <div class="field"><label>Phone Number *</label><div></div></div>
    <div class="field"><label>How Can We Help?</label><div></div></div>
    <a class="btn submit">Request A Free Quote</a>
  </form>
</section>

<section class="features">
  <div class="feature" style="left:100px">
    <svg width="36" height="36" viewBox="0 0 24 24"><path fill="#fff" d="M10 3h4v3h3v4h3v4h-3v7H7v-7H4v-4h3V6h3z"/></svg>
    <span>Hassle Free<br>Process</span>
  </div>
  <div class="feature" style="left:300px">
    <svg width="38" height="36" viewBox="0 0 26 24"><rect x="4" y="4" width="18" height="12" rx="1" fill="none" stroke="#fff" stroke-width="2"/><path d="M1 19h24" stroke="#fff" stroke-width="2"/></svg>
    <span>Book Online - Confirmed &amp; Locked<br>In Within 60 Seconds</span>
  </div>
  <div class="feature" style="left:674px">
    <svg width="36" height="36" viewBox="0 0 24 24"><circle cx="12" cy="12" r="10" fill="none" stroke="#fff" stroke-width="2"/><path d="M12 6v6l4 3" stroke="#fff" stroke-width="2" fill="none"/></svg>
    <span>On Time -<br>Every Time</span>
  </div>
  <div class="feature" style="left:886px">
    <svg width="40" height="36" viewBox="0 0 28 24"><path fill="#fff" d="M1 5h15v11H1zM17 9h5l4 4v3h-9z"/><circle cx="6" cy="18" r="2.5" fill="#fff"/><circle cx="21" cy="18" r="2.5" fill="#fff"/></svg>
    <span>Project delivered on<br>time-guaranteed</span>
  </div>
</section>

<section class="intro">
  <div class="photo" role="img" aria-label="Company trucks and woodchipper parked on a suburban street"></div>
  <svg class="play" width="36" height="36" viewBox="0 0 36 36"><circle cx="18" cy="18" r="18" fill="#fff"/><path d="M14 11l11 7-11 7z" fill="#e3312a"/></svg>
  <div class="copy">
    <p>Looking for a RELIABLE tree lopper with competitive pricing? Marlo can come out to you very fast to give you a free no obligation consultation. We will look after you through the whole process so don't have to stress.</p>
    <p>We'll make those trees safe and look a lot better so you can relax, feel safe and know the job will be done properly with Perth's best tree removal company. We specialize in tight access tree removals.</p>
  </div>
  <a class="btn" style="left:598px;top:355px;width:140px;height:32px;font-size:13px">Enquire Now</a>
</section>

<section class="services">
  <div class="photo" role="img" aria-label="Faded portrait of an arborist in a hard hat and hi-vis shirt"></div>
  <h2 class="section-title" style="top:66px">Our Services</h2>
  <div class="rule" style="top:118px"></div>

  <div class="service" style="left:100px;top:185px">
    <div class="icon"><svg width="44" height="44" viewBox="0 0 24 24"><path fill="#fff" d="M12 2l6 8h-3l4 6h-6v6h-2v-6H5l4-6H6z"/></svg></div>
    <h4>Tree<br>Removal</h4>
    <p>Removing a tree from your property can be a risky and dangerous task. We have highly experienced arborists that can tackle any task and will dismantle a tree in a safe</p>
  </div>
  <div class="service" style="left:460px;top:185px">
    <div class="icon"><svg width="44" height="44" viewBox="0 0 24 24"><rect x="3" y="6" width="18" height="10" rx="3" fill="#fff"/><circle cx="7" cy="18" r="2.5" fill="#fff"/><circle cx="17" cy="18" r="2.5" fill="#fff"/></svg></div>
    <h4>Stump<br>Grinding</h4>
    <p>Our machines can get to 95% of all stumps where access is limited. We can remove stumps of all sizes without causing any damage to your property.</p>
  </div>
  <div class="service" style="left:820px;top:185px">
    <div class="icon"><svg width="44" height="44" viewBox="0 0 24 24"><circle cx="10" cy="10" r="6" fill="none" stroke="#fff" stroke-width="2.5"/><path d="M14.5 14.5L21 21" stroke="#fff" stroke-width="3"/></svg></div>
    <h4>Tree<br>Inspections</h4>
    <p>Is your trees looking worse for wear? We can come and inspect your trees for to see if they have pest or diseases</p>
  </div>
  <div class="service" style="left:100px;top:427px">
    <div class="icon"><svg width="44" height="44" viewBox="0 0 24 24"><path d="M12 2v20M5 6h14M7 11h10M4 6l3 5M20 6l-3 5" stroke="#fff" stroke-width="2" fill="none"/></svg></div>
    <h4>Power Line<br>Clearances</h4>
    <p>Our boys are trained to work near power lines and will prune your trees so they are safe from buildings and meet network power regulations</p>
  </div>
  <div class="service" style="left:460px;top:427px">
    <div class="icon"><svg width="44" height="44" viewBox="0 0 24 24"><path fill="#fff" d="M3 16h12v-5h3l3 5v3H3z"/><path d="M10 11L5 4l-2 2" stroke="#fff" stroke-width="2" fill="none"/></svg></div>
    <h4>Land<br>Clearing</h4>
    <p>We can remove all trees from a block in preparation for subdividing. Large excavators can only do so much when it comes to dismantling big trees. They often require</p>
  </div>
  <div class="service" style="left:820px;top:427px">
    <div class="icon"><svg width="44" height="44" viewBox="0 0 24 24"><circle cx="6" cy="18" r="3" fill="none" stroke="#fff" stroke-width="2"/><circle cx="18" cy="18" r="3" fill="none" stroke="#fff" stroke-width="2"/><path d="M8 16L17 3M16 16L7 3" stroke="#fff" stroke-width="2"/></svg></div>
    <h4 style="top:30px">Pruning</h4>
    <p>There's a lot of reasons for pruning, thinning canopies to improve light penetration, weight reduction, balancing canopy and many more. Let our experts sort it for you</p>
  </div>
</section>

<section class="banner">
  <div class="photo" role="img" aria-label="Dusky view of tall trees against the evening sky"></div>
  <h2>PROFESSIONALISM. POLITE. HONEST.</h2>
  <p>Just 3 of the many qualities of Kestrel Grove tree surgeons. Knowing that your with a company<br>that will get the job done on time takes all the stress away.</p>
  <a class="btn" style="left:497px;top:232px;width:203px;height:64px;flex-direction:column;font-size:13px;line-height:18px">Click to Contact Us<span>0491 570 156</span></a>
</section>

<section class="guarantee">
  <div class="panel"></div>
  <div class="badge" role="img" aria-label="Satisfaction guarantee seal"></div>
  <h3 style="left:212px;top:94px;width:360px">Your project is backed by our customer satisfaction guaranteed.</h3>
  <div class="body">
    <p>All work is covered by our customer satisfaction. That means if your not happy with the job, we will come back and make it right. You have nothing to lose.</p>
    <p>Yes I want a FREE no obligation quote from Kestrel Grove tree surgeons</p>
  </div>
  <a class="btn" style="left:100px;top:385px;width:178px;height:38px;text-transform:none;font-size:15px">Book Online Now</a>
  <div class="photo ebook" role="img" aria-label="Cover of the ebook 20 Steps for Healthy Trees"></div>
  <h3 style="left:848px;top:102px;width:260px;font-weight:700;line-height:34px">We have a ebook on the 20 steps for healthy trees and it's totally free</h3>
  <a class="btn" style="left:848px;top:311px;width:250px;height:41px;text-transform:none;font-size:15px">Download The Guide Now</a>
</section>

<section class="testimonials">
  <h2 class="section-title" style="top:88px">What do our clients say?</h2>
  <svg class="arrow" style="left:118px" width="24" height="40" viewBox="0 0 24 40"><path d="M20 4L4 20l16 16" stroke="#555" stroke-width="4" fill="none"/></svg>
  <svg class="arrow" style="left:1054px" width="24" height="40" viewBox="0 0 24 40"><path d="M4 4l16 16L4 36" stroke="#555" stroke-width="4" fill="none"/></svg>
  <div class="photo avatar" role="img" aria-label="Portrait of the client"></div>
  <span class="qmark" style="left:400px;top:160px">“</span>
  <p class="testimonial-text">We used Kestrel Grove to remove a row of pencil pines that were overgrown and in a difficult location around the pool. We were extremely satisfied with Marlo and his team, prompt service , professional from first contact to cleanup. you can't fault these guys I would use Kestrel again and highly recommend them.</p>
  <p class="testimonial-name">Dean Hollis, Kestrel Grove tree surgeons</p>
  <span class="qmark" style="left:820px;top:275px">”</span>
</section>

<section class="blog">
  <h2 class="section-title" style="top:58px">Latest Blog</h2>
  <div class="photo" role="img" aria-label="Arborist working up a tall palm tree beside a house"></div>
  <h3>Sed ut perspiciatis unde omnis iste natus</h3>
  <div class="meta"><span>📅 March 25, 2018</span><span>2 comments</span></div>
  <p class="excerpt">Sed ut perspiciatis unde omnis iste natus error sit voluptatem accusantium doloremque laudantium, totam rem aperiam, eaque ipsa quae ab illo inventore veritatis et quasi architecto beatae vitae dicta sunt explicabo. Nemo enim ipsam voluptatem quia voluptas sit aspernatur aut odit aut fugit, sed quia consequuntur magni dolores eos qui ratione voluptatem sequi nesciunt. Neque porro quisquam est.</p>
  <p class="more">READ MORE &gt;&gt;</p>
</section>

<section class="callband">
  <svg class="abs" style="left:100px;top:26px" width="20" height="32" viewBox="0 0 20 32"><rect x="2" y="1" width="16" height="30" rx="3" fill="none" stroke="#fff" stroke-width="2"/><circle cx="10" cy="26" r="1.5" fill="#fff"/></svg>
  <div class="label" style="left:135px"><b>CALL NOW</b><br>for free consultation</div>
  <div class="value" style="left:305px">: 0491 570 156</div>
  <div class="or">OR</div>
  <svg class="abs" style="left:623px;top:30px" width="30" height="24" viewBox="0 0 30 24"><rect x="1" y="1" width="28" height="22" fill="none" stroke="#fff" stroke-width="2"/><path d="M1 1l14 12L29 1" stroke="#fff" stroke-width="2" fill="none"/></svg>
  <div class="label" style="left:662px"><b>MAIL US NOW</b><br>for free consultation</div>
  <div class="value" style="left:820px">: quotes@kestrelgroveprune.com.au</div>
</section>

<footer class="site-footer">
  <div class="footer-brand"><span class="brand-mark"></span><span class="brand-name">Kestrel Grove Tree Surgeons</span></div>
  <h4 style="left:352px">Sign up for newsletter</h4>
  <p class="small" style="left:352px;top:102px">Enter your email &amp; subscribing newsletter</p>
  <div class="newsletter">
    <div class="input"><svg width="16" height="12" viewBox="0 0 16 12"><rect x=".5" y=".5" width="15" height="11" fill="none" stroke="#aaa"/><path d="M.5.5L8 7l7.5-6.5" stroke="#aaa" fill="none"/></svg>Email address</div>
    <a class="btn">Subscribe</a>
  </div>
  <div class="socials"><span></span><span style="background:#3aa4dc"></span><span style="background:#d8433a"></span></div>
  <h4 style="left:720px">Contact us</h4>
  <svg class="abs" style="left:722px;top:106px" width="14" height="18" viewBox="0 0 14 18"><path d="M7 0a7 7 0 0 0-7 7c0 5 7 11 7 11s7-6 7-11a7 7 0 0 0-7-7z" fill="#1fa54a"/><circle cx="7" cy="7" r="2.5" fill="#fff"/></svg>
  <p class="small" style="left:746px;top:104px;line-height:20px">Address:<br>14 Larkspur Way Ridgefield<br>6070</p>
  <h4 style="left:988px">Quick links</h4>
  <ul class="links"><li>Home</li><li>Services</li><li>About Us</li><li>News</li><li>Contact us</li></ul>
</footer>

<div class="copyright">©2018 Kestrel Grove tree surgeons . All Rights Reserved.</div>

</body>
</html>
```